Page for a flyer

I need a page designed that is 8.5" wide and 5.5" height. I need the left half of the page to be vintage looking in color and texture and the other half to be plain white and look like it is ripped down the middle

```html
<!DOCTYPE html>
<html lang="en">
<head>
<meta charset="utf-8">
<title>Flyer Page – Vintage and Torn White</title>
<style>
  :root {
    --backdrop: #363636;
    --paper-white: #ffffff;
    --vintage-light: #fbf6e6;
    --vintage-mid: #efe4cb;
    --vintage-deep: #dccaa3;
    --tear-shadow: rgba(0, 0, 0, 0.28);
  }
  html, body {
    margin: 0;
    padding: 0;
    width: 1200px;
    height: 1200px;
    overflow: hidden;
    background: var(--backdrop);
  }
  .canvas {
    position: relative;
    width: 1200px;
    height: 1200px;
  }
  .flyer-page {
    position: absolute;
    left: 83px;
    top: 260px;
    width: 1034px;
    height: 679px;
    box-shadow: 0 8px 24px rgba(0, 0, 0, 0.45);
  }
  .flyer-page svg {
    display: block;
    width: 100%;
    height: 100%;
  }
</style>
</head>
<body>
<main class="canvas">
  <section class="flyer-page" aria-label="Flyer page, vintage left half and torn plain white right half">
    <svg viewBox="0 0 1034 679" xmlns="http://www.w3.org/2000/svg">
      <defs>
        <radialGradient id="vintageGlow" cx="0.35" cy="0.28" r="0.85">
          <stop offset="0" stop-color="var(--vintage-light)"/>
          <stop offset="0.55" stop-color="var(--vintage-mid)"/>
          <stop offset="1" stop-color="var(--vintage-deep)"/>
        </radialGradient>
        <linearGradient id="vintageEdges" x1="0" y1="0" x2="0" y2="1">
          <stop offset="0" stop-color="#d8c59c" stop-opacity="0.45"/>
          <stop offset="0.12" stop-color="#d8c59c" stop-opacity="0"/>
          <stop offset="0.85" stop-color="#d8c59c" stop-opacity="0"/>
          <stop offset="1" stop-color="#d3bd8f" stop-opacity="0.45"/>
        </linearGradient>
        <filter id="tearShadow" x="-20%" y="-5%" width="160%" height="110%">
          <feDropShadow dx="5" dy="2" stdDeviation="4" flood-color="#000" flood-opacity="0.28"/>
        </filter>
      </defs>

      <rect class="page-white" x="0" y="0" width="1034" height="679" fill="var(--paper-white)"/>

      <g class="vintage-half" role="img" aria-label="Aged vintage paper texture in cream and tan tones">
        <path id="vintageShape" fill="url(#vintageGlow)"
          d="M0 0 H534 L537 40 L531 80 L528 120 L520 160 L524 190 L516 230 L512 262 L516 300 L520 340 L517 380 L524 420 L521 460 L529 500 L526 540 L519 580 L514 620 L517 660 L520 679 H0 Z"/>
        <path fill="url(#vintageEdges)"
          d="M0 0 H534 L537 40 L531 80 L528 120 L520 160 L524 190 L516 230 L512 262 L516 300 L520 340 L517 380 L524 420 L521 460 L529 500 L526 540 L519 580 L514 620 L517 660 L520 679 H0 Z"/>
      </g>

      <path class="torn-lip" fill="var(--paper-white)" filter="url(#tearShadow)"
        d="M537 0 L540 40 L534 80 L531 120 L523 160 L527 190 L519 230 L515 262 L519 300 L523 340 L520 380 L527 420 L524 460 L532 500 L529 540 L522 580 L517 620 L520 660 L523 679
           L531 679 L528 660 L526 640 L531 620 L533 600 L541 580 L540 560 L546 540 L541 520 L546 500 L539 480 L543 460 L548 440 L554 420 L546 400 L550 380 L556 360 L550 340 L545 320 L540 300 L537 280 L534 262 L540 240 L532 220 L537 200 L533 180 L537 160 L540 140 L546 120 L548 100 L545 80 L552 60 L548 40 L553 20 L555 0 Z"/>
    </svg>
  </section>
</main>
</body>
</html>
```